Uregent Care opening postcard with coupon

We need a postcard created to mail directly to homes. The flyer need to be appealing and include a small spot with a coupon for $20 gift card with first visit. The post card needs to be 2 sided and 4X6. We have a logo. To learn more about us visit maplegroveclinicplus.example or check us out on facebook. I will try to figure out how to upload logo.

Target Market(s)

All households that need urgent care.

Industry/Entity Type

Healthcare

Font styles to use
Serif

Colors
33a6d7
447fba
85acd3
85cae6
cfdfed
ecf7fb

Requirements
Must have
• our logo
• family centered
• some services offered
• coupon with free $20 gc at first visit if you bring in this flyer
Nice to have
• visually appealing

```html
<!DOCTYPE html>
<html lang="en">
<head>
<meta charset="utf-8">
<title>Maple Grove Clinic Plus – Grand Opening Postcard</title>
<link rel="stylesheet" href="https://fonts.googleapis.com/css2?family=Cinzel:wght@600&family=Open+Sans:wght@400;600;700;800&family=Roboto+Condensed:wght@400;700&display=swap">
<style>
  :root {
    --navy: #110f52;
    --royal: #2f6fd6;
    --sky: #37a8dc;
    --panel: #a9c4e2;
    --white: #ffffff;
    --stage: #2f2f31;
    --stamp: #c8c8c8;
    --rule: #b9b9b9;
  }
  * { margin: 0; padding: 0; box-sizing: border-box; }
  html, body { width: 850px; height: 1200px; overflow: hidden; }
  body { background: var(--stage); position: relative; font-family: "Open Sans", sans-serif; }

  .postcard { position: absolute; background: var(--white); overflow: hidden; }
  .postcard--front { left: 157px; top: 97px; width: 535px; height: 411px; }
  .postcard--back  { left: 157px; top: 614px; width: 530px; height: 408px; }

  /* FRONT */
  .family-photo {
    position: absolute; left: 150px; top: 28px; width: 385px; height: 320px;
    background: linear-gradient(180deg, #dfe7ee 0%, #b9ccd8 25%, #9db4c0 45%, #c9c2b6 70%, #e4ddd3 100%);
  }
  .front-band { position: absolute; left: 0; top: 0; width: 535px; height: 411px; }
  .opening-ribbon {
    position: absolute; left: 19px; top: 0; width: 186px; height: 232px;
    background: var(--sky);
    clip-path: polygon(0 0, 100% 0, 100% 92%, 50% 100%, 0 92%);
    text-align: center;
  }
  .opening-ribbon__title {
    font-family: "Cinzel", serif; font-weight: 600; color: var(--navy);
    font-size: 33px; line-height: 32px; margin-top: 22px;
    border-top: 1px solid rgba(255,255,255,.6); border-bottom: 1px solid rgba(255,255,255,.6);
    margin-left: 8px; margin-right: 8px; padding: 2px 0 4px;
  }
  .opening-ribbon__date { font-weight: 700; color: var(--white); font-size: 18px; margin-top: 10px; }
  .opening-ribbon__days { font-family: "Roboto Condensed", sans-serif; font-weight: 700; color: var(--navy); font-size: 17px; margin-top: 4px; }
  .opening-ribbon__hours { font-family: "Roboto Condensed", sans-serif; font-weight: 700; color: var(--white); font-size: 17px; margin-top: 4px; }

  .brand-name {
    position: absolute; display: flex; align-items: center; gap: 8px;
    font-family: "Roboto Condensed", sans-serif; font-weight: 700; color: var(--navy); line-height: 1;
  }
  .brand-name__mark { background: var(--navy); flex: none; }
  .brand-name--front { left: 282px; top: 26px; font-size: 23px; }
  .brand-name--front .brand-name__mark { width: 30px; height: 30px; }
  .brand-name--back { left: 252px; top: 38px; font-size: 17px; }
  .brand-name--back .brand-name__mark { width: 22px; height: 22px; }

  .front-contact { position: absolute; left: 18px; top: 281px; color: var(--white); font-size: 15px; line-height: 22px; }
  .contact-line { display: flex; align-items: center; gap: 7px; color: var(--white); }
  .contact-line svg { flex: none; }
  .contact-line--phone { position: absolute; left: 17px; top: 350px; font-size: 21px; }
  .contact-line--web { position: absolute; left: 17px; top: 380px; font-size: 14px; }
  .front-address { position: absolute; left: 289px; top: 354px; color: var(--white); font-size: 17px; line-height: 26px; display: flex; gap: 9px; }
  .front-address svg { margin-top: 4px; flex: none; }

  /* BACK */
  .services-panel { position: absolute; left: 0; top: 0; width: 246px; height: 341px; background: var(--panel); }
  .services-title {
    position: absolute; left: 18px; top: 10px; width: 180px;
    font-family: "Roboto Condensed", sans-serif; font-weight: 700; font-size: 21px; color: var(--navy);
    border-bottom: 1.5px solid var(--navy); padding-bottom: 1px;
  }
  .services-list { position: absolute; left: 18px; top: 44px; list-style: none; color: var(--navy); font-size: 13.5px; line-height: 18.3px; }
  .services-list li { display: flex; gap: 5px; }
  .services-list li svg { flex: none; margin-top: 5px; }
  .back-band { position: absolute; left: 0; top: 0; width: 246px; height: 341px; }
  .coupon {
    position: absolute; left: 128px; top: 216px; width: 112px; height: 74px;
    background: var(--royal); border: 3px solid var(--white); border-radius: 10px;
    color: var(--white); box-shadow: 0 2px 4px rgba(0,0,0,.3);
  }
  .coupon__free { position: absolute; left: 8px; top: 0; font-weight: 800; font-size: 22px; letter-spacing: .5px; }
  .coupon__amount { position: absolute; left: 7px; top: 27px; font-weight: 800; font-size: 23px; }
  .coupon__terms { position: absolute; left: 55px; top: 34px; font-weight: 700; font-size: 8px; line-height: 10px; }
  .back-contact { position: absolute; left: 13px; top: 287px; color: var(--white); }
  .back-contact__title { font-size: 15px; line-height: 20px; }
  .back-contact .contact-line { font-size: 12px; line-height: 17px; }
  .back-contact .contact-line--small { font-size: 11px; }
  .stamp-box { position: absolute; left: 431px; top: 18px; width: 76px; height: 76px; background: var(--stamp); }
  .address-lines { position: absolute; left: 283px; top: 150px; width: 224px; }
  .address-lines span { display: block; height: 1px; background: var(--rule); margin-bottom: 21px; }
</style>
</head>
<body>

<section class="postcard postcard--front">
  <div class="family-photo" role="img" aria-label="Photo of a smiling family of four on a sunny beach"></div>

  <svg class="front-band" viewBox="0 0 535 411" aria-hidden="true">
    <path d="M0,252 C120,225 250,262 535,330 L535,345 C260,290 130,250 0,262 Z" fill="var(--royal)"/>
    <path d="M0,262 C130,250 260,290 535,345 L535,411 L0,411 Z" fill="var(--navy)"/>
  </svg>

  <div class="opening-ribbon">
    <div class="opening-ribbon__title">Grand<br>Opening</div>
    <div class="opening-ribbon__date">OCTOBER 9TH</div>
    <div class="opening-ribbon__days">MONDAY TO SATURDAY</div>
    <div class="opening-ribbon__hours">7AM-7PM</div>
    <div class="opening-ribbon__hours">SUNDAY 10AM- 7PM</div>
  </div>

  <div class="brand-name brand-name--front"><span class="brand-name__mark"></span><span>Maple Grove<br>Clinic Plus</span></div>

  <p class="front-contact">Contact Us To Schedule<br>Appointment Today.<br>Call Us :</p>
  <div class="contact-line contact-line--phone">
    <svg width="15" height="15" viewBox="0 0 16 16"><circle cx="8" cy="8" r="7" fill="none" stroke="#fff" stroke-width="1.4"/><path d="M5.3 4.3l1.4-.3.8 2-1 .8c.4.9 1 1.5 1.9 1.9l.8-1 2 .8-.3 1.4c-3 .4-6-2.6-5.6-5.6z" fill="#fff"/></svg>
    <span>(555) 014-2273</span>
  </div>
  <div class="contact-line contact-line--web">
    <svg width="15" height="15" viewBox="0 0 16 16"><circle cx="8" cy="8" r="7" fill="none" stroke="#fff" stroke-width="1.3"/><path d="M1 8h14M8 1c-3 3.5-3 10.5 0 14M8 1c3 3.5 3 10.5 0 14M2.5 4.5h11M2.5 11.5h11" fill="none" stroke="#fff" stroke-width="1"/></svg>
    <span>www.maplegroveclinicplus.example</span>
  </div>
  <div class="front-address">
    <svg width="17" height="17" viewBox="0 0 16 16"><circle cx="8" cy="8" r="7" fill="none" stroke="#fff" stroke-width="1.3"/><path d="M8 3.5a2.8 2.8 0 0 0-2.8 2.8C5.2 8.5 8 12 8 12s2.8-3.5 2.8-5.7A2.8 2.8 0 0 0 8 3.5z" fill="#fff"/><circle cx="8" cy="6.3" r="1" fill="var(--navy)"/></svg>
    <span>1820 Harbor Lane<br>Fairview, Virginia 20100</span>
  </div>
</section>

<section class="postcard postcard--back">
  <div class="services-panel"></div>
  <svg class="back-band" viewBox="0 0 246 341" aria-hidden="true">
    <path d="M0,270 C70,262 150,282 246,298 L246,306 C150,290 70,272 0,280 Z" fill="var(--royal)"/>
    <path d="M0,280 C70,272 150,290 246,306 L246,341 L0,341 Z" fill="var(--navy)"/>
  </svg>

  <h2 class="services-title">Services We Offer:</h2>
  <ul class="services-list">
    <li><svg width="9" height="9" viewBox="0 0 10 10"><rect x=".6" y=".6" width="8.8" height="8.8" fill="none" stroke="var(--navy)" stroke-width="1.2"/><path d="M2.3 5l1.8 1.8 3.6-3.8" fill="none" stroke="var(--navy)" stroke-width="1.4"/></svg><span>Urgent Care</span></li>
    <li><svg width="9" height="9" viewBox="0 0 10 10"><rect x=".6" y=".6" width="8.8" height="8.8" fill="none" stroke="var(--navy)" stroke-width="1.2"/><path d="M2.3 5l1.8 1.8 3.6-3.8" fill="none" stroke="var(--navy)" stroke-width="1.4"/></svg><span>Medication Refills</span></li>
    <li><svg width="9" height="9" viewBox="0 0 10 10"><rect x=".6" y=".6" width="8.8" height="8.8" fill="none" stroke="var(--navy)" stroke-width="1.2"/><path d="M2.3 5l1.8 1.8 3.6-3.8" fill="none" stroke="var(--navy)" stroke-width="1.4"/></svg><span>Lab Tests &amp; Vaccinations</span></li>
    <li><svg width="9" height="9" viewBox="0 0 10 10"><rect x=".6" y=".6" width="8.8" height="8.8" fill="none" stroke="var(--navy)" stroke-width="1.2"/><path d="M2.3 5l1.8 1.8 3.6-3.8" fill="none" stroke="var(--navy)" stroke-width="1.4"/></svg><span>Well Exams</span></li>
    <li><svg width="9" height="9" viewBox="0 0 10 10"><rect x=".6" y=".6" width="8.8" height="8.8" fill="none" stroke="var(--navy)" stroke-width="1.2"/><path d="M2.3 5l1.8 1.8 3.6-3.8" fill="none" stroke="var(--navy)" stroke-width="1.4"/></svg><span>Health Screenings</span></li>
    <li><svg width="9" height="9" viewBox="0 0 10 10"><rect x=".6" y=".6" width="8.8" height="8.8" fill="none" stroke="var(--navy)" stroke-width="1.2"/><path d="M2.3 5l1.8 1.8 3.6-3.8" fill="none" stroke="var(--navy)" stroke-width="1.4"/></svg><span>Pediatrics</span></li>
    <li><svg width="9" height="9" viewBox="0 0 10 10"><rect x=".6" y=".6" width="8.8" height="8.8" fill="none" stroke="var(--navy)" stroke-width="1.2"/><path d="M2.3 5l1.8 1.8 3.6-3.8" fill="none" stroke="var(--navy)" stroke-width="1.4"/></svg><span>Infections</span></li>
    <li><svg width="9" height="9" viewBox="0 0 10 10"><rect x=".6" y=".6" width="8.8" height="8.8" fill="none" stroke="var(--navy)" stroke-width="1.2"/><path d="M2.3 5l1.8 1.8 3.6-3.8" fill="none" stroke="var(--navy)" stroke-width="1.4"/></svg><span>Preventive Services</span></li>
    <li><svg width="9" height="9" viewBox="0 0 10 10"><rect x=".6" y=".6" width="8.8" height="8.8" fill="none" stroke="var(--navy)" stroke-width="1.2"/><path d="M2.3 5l1.8 1.8 3.6-3.8" fill="none" stroke="var(--navy)" stroke-width="1.4"/></svg><span>School and Sport<br>Physicals</span></li>
    <li><svg width="9" height="9" viewBox="0 0 10 10"><rect x=".6" y=".6" width="8.8" height="8.8" fill="none" stroke="var(--navy)" stroke-width="1.2"/><path d="M2.3 5l1.8 1.8 3.6-3.8" fill="none" stroke="var(--navy)" stroke-width="1.4"/></svg><span>On-site X-Rays</span></li>
  </ul>

  <div class="coupon">
    <span class="coupon__free">FREE</span>
    <span class="coupon__amount">$20</span>
    <span class="coupon__terms">GIFT CARD<br>WITH FIRST<br>VISIT</span>
  </div>

  <div class="back-contact">
    <p class="back-contact__title">Contact Us:</p>
    <div class="contact-line">
      <svg width="11" height="11" viewBox="0 0 16 16"><circle cx="8" cy="8" r="7" fill="none" stroke="#fff" stroke-width="1.6"/><path d="M5.3 4.3l1.4-.3.8 2-1 .8c.4.9 1 1.5 1.9 1.9l.8-1 2 .8-.3 1.4c-3 .4-6-2.6-5.6-5.6z" fill="#fff"/></svg>
      <span>(555) 014-2273</span>
    </div>
    <div class="contact-line contact-line--small">
      <svg width="11" height="11" viewBox="0 0 16 16"><circle cx="8" cy="8" r="7" fill="none" stroke="#fff" stroke-width="1.5"/><path d="M1 8h14M8 1c-3 3.5-3 10.5 0 14M8 1c3 3.5 3 10.5 0 14" fill="none" stroke="#fff" stroke-width="1.1"/></svg>
      <span>www.maplegroveclinicplus.example</span>
    </div>
  </div>

  <div class="brand-name brand-name--back"><span class="brand-name__mark"></span><span>Maple Grove<br>Clinic Plus</span></div>
  <div class="stamp-box"></div>
  <div class="address-lines"><span></span><span></span><span></span><span></span></div>
</section>

</body>
</html>
```